Note Cards for Clients

Hi - I need a design for simple flat note-cards and envelopes to use to send clients a written note in a professional manner. Please use my logo and color scheme.

Hi again- sorry for the miscommunication. I'd like to have note-cards 5x8 with envelopes as opposed to traditional stationary samples.

Thanks!

It Professional

```html
<!DOCTYPE html>
<html lang="en">
<head>
<meta charset="utf-8">
<title>Halvern Wealth Partners – Envelope</title>
<link rel="stylesheet" href="https://fonts.googleapis.com/css2?family=EB+Garamond:wght@400;500&display=swap">
<style>
  :root {
    --paper: #ffffff;
    --dieline: #111111;
    --brand-blue: #1f3fae;
    --brand-grey: #6d7072;
    --ink: #1a1a1a;
  }
  html, body {
    margin: 0;
    padding: 0;
    width: 1200px;
    height: 812px;
    overflow: hidden;
    background: var(--paper);
  }
  .envelope {
    position: relative;
    width: 1200px;
    height: 812px;
    background: var(--paper);
  }
  .envelope__dieline {
    position: absolute;
    inset: 0;
  }
  .return-block {
    position: absolute;
    top: 108px;
    left: 0;
    width: 1200px;
    text-align: center;
    font-family: "EB Garamond", Georgia, serif;
    color: var(--ink);
  }
  .brand {
    display: inline-flex;
    align-items: center;
    gap: 12px;
    height: 70px;
  }
  .brand__square {
    width: 46px;
    height: 46px;
    background: var(--brand-blue);
  }
  .brand__name {
    font-family: "EB Garamond", Georgia, serif;
    font-weight: 500;
    font-size: 34px;
    letter-spacing: 1px;
    color: var(--brand-blue);
    line-height: 1;
  }
  .return-address {
    margin: 6px 0 0;
    font-size: 19px;
    line-height: 28px;
    font-style: normal;
  }
</style>
</head>
<body>
  <main class="envelope">
    <svg class="envelope__dieline" viewBox="0 0 1200 812" width="1200" height="812" aria-hidden="true">
      <g fill="none" stroke="var(--dieline)" stroke-width="1.6">
        <rect x="1" y="1" width="1198" height="810"/>
        <polyline points="2,14 54,444 1142,444 1197,14"/>
        <line x1="54" y1="444" x2="4" y2="811"/>
        <line x1="1142" y1="444" x2="1197" y2="811"/>
      </g>
    </svg>

    <header class="return-block">
      <div class="brand">
        <span class="brand__square"></span>
        <span class="brand__name">HALVERN WEALTH PARTNERS, LLC</span>
      </div>
      <address class="return-address">
        5678 Harbor Avenue, Suite CD<br>
        Coral Bay, FL 33210
      </address>
    </header>
  </main>
</body>
</html>
```